Australian Software Consultancy needs new Business Card Design

Design Business Card based on existing design artefacts (attached). We are open to all designs. As its a 2 sided design and we thought it might be quite striking to have one side with a black background and te other side with a white background.

Target Market(s)

Financial Services mainly.

Industry/Entity Type

Business

Contact Information for Business Card

Name :
Position :
Email :

Requirements
Must have
• Funky design using our existing assets

```html
<!DOCTYPE html>
<html lang="en">
<head>
<meta charset="utf-8">
<title>Deep Signal – Business Card</title>
<link rel="stylesheet" href="https://fonts.googleapis.com/css2?family=Montserrat:wght@700&family=Lato:wght@400;700&display=swap">
<style>
  :root {
    --page-bg: #3a3a3a;
    --card-black: #1b1b1c;
    --card-white: #f1f1f1;
    --brand-red: #e0222b;
    --text-white: #f2f2f2;
    --text-grey: #cfcfcf;
    --text-dark: #141414;
  }
  * { box-sizing: border-box; margin: 0; padding: 0; }
  html, body {
    width: 1200px; height: 834px; overflow: hidden;
    background: var(--page-bg);
  }
  .sheet {
    position: relative; width: 1200px; height: 834px;
    display: flex; flex-direction: column; align-items: center;
    justify-content: center; gap: 40px;
  }
  .card {
    position: relative; width: 620px; height: 354px;
    box-shadow: 0 12px 30px rgba(0,0,0,0.45);
    overflow: hidden;
  }
  .card-front {
    background: var(--card-black);
    display: flex; align-items: center; justify-content: center;
  }
  .wordmark {
    font-family: "Montserrat", sans-serif; font-weight: 700;
    letter-spacing: 1px; text-transform: uppercase; line-height: 1;
    white-space: nowrap;
  }
  .card-front .wordmark { font-size: 50px; color: var(--text-white); }

  .card-back { display: flex; background: var(--card-black); }
  .back-brand {
    position: relative; width: 310px; height: 100%;
    background: var(--card-white);
    display: flex; align-items: center; justify-content: center;
    padding-top: 40px;
  }
  .back-brand .wordmark { font-size: 30px; color: var(--text-dark); }
  .split-notch {
    position: absolute; left: 300px; top: 167px; width: 0; height: 0;
    border-top: 10px solid transparent; border-bottom: 10px solid transparent;
    border-right: 10px solid var(--card-black);
  }
  .back-contact {
    flex: 1; padding-left: 70px;
    display: flex; flex-direction: column; justify-content: center;
    font-family: "Lato", sans-serif;
  }
  .person-name { font-size: 20px; font-weight: 700; color: var(--text-white); }
  .person-role { font-size: 16px; color: var(--brand-red); margin-bottom: 16px; }
  .contact-line {
    display: flex; align-items: center; gap: 14px;
    font-size: 15px; color: var(--text-grey); margin-top: 4px;
  }
  .contact-line svg { width: 16px; height: 16px; flex: none; }
</style>
</head>
<body>
<main class="sheet">
  <section class="card card-front">
    <p class="wordmark">Deep Signal</p>
  </section>

  <section class="card card-back">
    <div class="back-brand">
      <p class="wordmark">Deep Signal</p>
    </div>
    <span class="split-notch"></span>
    <div class="back-contact">
      <p class="person-name">Alex Carter</p>
      <p class="person-role">President</p>
      <p class="contact-line">
        <svg viewBox="0 0 16 16" aria-hidden="true"><path d="M4 1.5l2.2 3-1.4 1.6c.8 2 2.3 3.5 4.3 4.3l1.6-1.4 3 2.2-1.4 2.6C7.2 13.6 2.4 8.8 1.4 3z" fill="none" stroke="#e0222b" stroke-width="1.3" stroke-linejoin="round"/></svg>
        9800 415 262
      </p>
      <p class="contact-line">
        <svg viewBox="0 0 16 16" aria-hidden="true"><rect x="1.5" y="3.5" width="13" height="9" fill="none" stroke="#e0222b" stroke-width="1.3"/><path d="M1.5 3.5L8 9l6.5-5.5" fill="none" stroke="#e0222b" stroke-width="1.3"/></svg>
        alex@mailbox.com
      </p>
    </div>
  </section>
</main>
</body>
</html>
```